Vitamin C Serum Packaging and Label re-design

Redesign exciting packaging and label re-design
naturals
Vitamin C 20%
E & Hyaluronic Acid
PROFESSIONAL Facial Serum
1 fl oz / 30ml
Ingredients: Aqua,Glycerin,Propylene Glycol,Sodium Hyaluronate,Niacinamide,Carbomer,Triethanolamine,Betaglucan,Ascorbic Acid, Ethylhexylglycerin,Caprylyl Glycol,Propanediol,Phenylpropanol.
72% Organic
FOR EXTERNAL USE ONLY
MADE IN CHINA
Product Description
Vitamin C serum has the Anti Aging power of Vitamin C + E + Amino + Hyaluronic Acid. Bold Lantern Skin Care gives you the highest quality Vitamin C Serum on the market with 98% Natural & 72% Organic ingredients.
Our 20% Vitamin C Serum Provides Your Skin With The Following Benefits:
1- Stimulates the production of collagen which makes your skin more vibrant, firm and youthful.
2- Contains Antioxidants that will greatly reduce skin damage caused by the sun, pollution and impurities in the air.
3- Enhances your skins rate of exfoliation for a smoother, brighter and more radiant complexion.
4- Greatly Diminishes the appearance of fine lines and wrinkles.
5- Has a high percentage of Hyaluronic Acid which deeply moisturizes the skin to reduce skin problems that occur due to age.
How to use
Dispense 2-3 drops into the palm of your hand and then apply to your face and neck. During the day, finish with a moisturizer with SPF 30 or greater. Can be applied under the eye area, avoiding the eye itself.
NON-IRRITATING, FRAGRANCE FREE, AND NEVER ANIMAL TESTED
Ingredients: Aqua, Ascorbic Acid (Vitamin C), Glycerin (Humectant), Sodium Hyaluronate (Hyaluronic Acid), Propylene Glycol (Humectant), Vitamin E, Niacinamide (Vitamin B3), Carbomer, Propanediol, Ethylhexylglycerin, Caprylyl Glycol, Phenylpropanol, Triethanolamine.
Store at 20- 75° C (68-77° F) Keep out of Direct Sunlight.
USA Company, Veteran owned and operated. 5% of sales will be donated to a nonprofit Veterans organization.
BoldLanternSkinCare.com
Target Market(s)
female and males for skin care product
Industry/Entity Type
Skin Care
Requirements
Must have
- Exciting logo.
Nice to have
- Army Green, Black, Gray colors to make it Sex Neutral. I want a fell of luxury and sophisticated packaging.

```html
<!DOCTYPE html>
<html lang="en">
<head>
<meta charset="utf-8">
<title>Bold Lantern Skin Care – Vitamin C Serum Packaging</title>
<link href="https://fonts.googleapis.com/css2?family=Cinzel:wght@400;600&family=Josefin+Sans:wght@300;400;600&family=Pathway+Gothic+One&display=swap" rel="stylesheet">
<style>
  :root{
    --bg:#dcdcdc;
    --green-deep:#17300d;
    --green:#234417;
    --green-glow:#5fae2a;
    --gold:#c9a24a;
    --gold-light:#e6c877;
    --cream:#e9e3c8;
    --white:#f2f2ee;
  }
  *{margin:0;padding:0;box-sizing:border-box}
  html,body{width:1200px;height:1200px;overflow:hidden;background:var(--bg)}
  .canvas{position:relative;width:1200px;height:1200px;background:radial-gradient(circle at 50% 40%,#ececec,var(--bg))}

  .carton{position:absolute;left:60px;top:50px;width:1080px;height:660px;display:flex;box-shadow:0 12px 30px rgba(0,0,0,.18)}
  .panel{width:270px;height:100%;background:var(--green-deep);border-right:1px solid rgba(201,162,74,.35);padding:34px 24px;color:var(--gold);position:relative}
  .panel:last-child{border-right:none}

  .copy{font-family:"Pathway Gothic One",sans-serif;font-size:15px;line-height:1.32;color:var(--gold)}
  .copy h3{font-size:22px;line-height:1.1;margin-bottom:6px;color:var(--gold-light);font-weight:400}
  .copy p{margin-bottom:10px}
  .copy ol{list-style:none}
  .copy li{margin-bottom:6px}
  .copy .caps{text-transform:uppercase;color:var(--gold-light)}

  .panel--front{background:radial-gradient(ellipse at 50% 58%,#3d7a1c 0%,var(--green) 40%,var(--green-deep) 80%);text-align:center;display:flex;flex-direction:column;align-items:center;padding-top:46px}
  .brand{display:flex;flex-direction:column;align-items:center;gap:10px}
  .brand-dot{width:22px;height:22px;border-radius:50%;background:var(--gold)}
  .brand-name{font-family:"Cinzel",serif;font-weight:400;color:var(--gold);text-transform:uppercase;text-align:center;line-height:1.15}
  .panel--front .brand-name{font-size:26px}
  .tagline{font-family:"Josefin Sans",sans-serif;font-weight:300;color:var(--gold);text-transform:uppercase;letter-spacing:.02em}
  .panel--front .tagline{font-size:12px;margin-top:12px}
  .vitamin-art{border-radius:50%;background:radial-gradient(circle at 50% 55%,#f3e27a 0%,#b9c932 28%,#4f9a1f 55%,rgba(35,68,23,0) 72%)}
  .panel--front .vitamin-art{width:230px;height:230px;margin-top:22px}
  .claim{border:1px solid var(--gold);font-family:"Josefin Sans",sans-serif;font-weight:300;color:var(--gold-light);line-height:1.25}
  .panel--front .claim{font-size:17px;padding:8px 12px;margin-top:18px}
  .skin{font-family:"Josefin Sans",sans-serif;font-weight:600;color:var(--white);letter-spacing:.12em;text-transform:uppercase}
  .panel--front .skin{font-size:15px;margin-top:26px}
  .volume{font-family:"Josefin Sans",sans-serif;font-weight:300;color:var(--gold-light)}
  .panel--front .volume{font-size:16px;margin-top:auto;margin-bottom:10px}

  .panel--back{display:flex;align-items:center;justify-content:center}
  .panel--back .brand-name{font-size:24px}

  .label{position:absolute;left:430px;top:750px;width:340px;height:410px;border-radius:6px;background:radial-gradient(ellipse at 50% 62%,#3d7a1c 0%,var(--green) 42%,var(--green-deep) 85%);box-shadow:0 10px 24px rgba(0,0,0,.18);display:flex;flex-direction:column;align-items:center;text-align:center;padding-top:26px}
  .label .brand-name{font-size:22px}
  .label .brand-dot{width:18px;height:18px}
  .label .tagline{font-size:10.5px;margin-top:8px}
  .label .vitamin-art{width:150px;height:150px;margin-top:8px}
  .label .claim{font-size:13px;padding:4px 10px;margin-top:6px}
  .label .skin{font-size:13px;font-weight:400;margin-top:10px}
  .label .volume{font-size:12px;margin-top:10px}
</style>
</head>
<body>
<div class="canvas">
  <section class="carton">
    <article class="panel panel--description copy">
      <h3>Product Description</h3>
      <p>Vitamin C serum has the Anti Aging power of Vitamin C + E + Amino + Hyaluronic Acid. Bold Lantern Skin Care gives you the highest quality Vitamin C Serum on the market with 98% Natural &amp; 72% Organic ingredients.</p>
      <h3>Our 20% Vitamin C Serum Provides Your Skin With The Following Benefits:</h3>
      <ol>
        <li>1. Stimulates the production of collagen which makes your skin more vibrant, firm and youthful.</li>
        <li>2. Contains Antioxidants that will greatly reduce skin damage caused by the sun, pollution and impurities in the air.</li>
        <li>3. Enhances your skins rate of exfoliation for a smoother, brighter and more radiant complexion.</li>
        <li>4. Greatly Diminishes the appearance of fine lines and wrinkles.</li>
        <li>5. Has a high percentage of Hyaluronic Acid which deeply moisturizes the skin to reduce skin problems that occur due to age.</li>
      </ol>
    </article>

    <article class="panel panel--front">
      <div class="brand"><span class="brand-dot"></span><span class="brand-name">Bold Lantern<br>Skin Care</span></div>
      <p class="tagline">Professional Day and Night Serum</p>
      <div class="vitamin-art" role="img" aria-label="Glowing golden serum drop with Vitamin C 20% capsule and orbiting molecules"></div>
      <p class="claim">with Vitamin E<br>&amp; Hyaluronic Acid</p>
      <p class="skin">All Skin Type</p>
      <p class="volume">1 fl oz / 30ml</p>
    </article>

    <article class="panel panel--usage copy">
      <h3>How to use</h3>
      <p>Dispense 2-3 drops into the palm of your hand and then apply to your face and neck. During the day, finish with a moisturizer with SPF 30 or greater. Can be applied under the eye area, avoiding the eye itself.</p>
      <p class="caps">Non-irritating, fragrance free, and never animal tested</p>
      <p>Ingredients: Aqua, Ascorbic Acid (Vitamin C), Glycerin (Humectant), Sodium Hyaluronate (Hyaluronic Acid), Propylene Glycol (Humectant), Vitamin E, Niacinamide (Vitamin B3), Carbomer, Propanediol, Ethylhexylglycerin, Caprylyl Glycol, Phenylpropanol, Triethanolamine.</p>
      <p>USA Company, Veteran owned and operated. 5% of sales will be donated to a nonprofit Veterans organization.</p>
      <p>Store at 20- 75° C (68-77° F) Keep out of Direct Sunlight.</p>
      <p>BoldLanternSkinCare.com</p>
    </article>

    <article class="panel panel--back">
      <div class="brand"><span class="brand-dot"></span><span class="brand-name">Bold Lantern<br>Skin Care</span></div>
    </article>
  </section>

  <section class="label">
    <div class="brand"><span class="brand-dot"></span><span class="brand-name">Bold Lantern<br>Skin Care</span></div>
    <p class="tagline">Professional Day and Night Serum</p>
    <div class="vitamin-art" role="img" aria-label="Glowing golden serum drop with Vitamin C 20% capsule and orbiting molecules"></div>
    <p class="claim">with Vitamin E &amp; Hyaluronic Acid</p>
    <p class="skin">All Skin Type</p>
    <p class="volume">1 fl oz / 30ml</p>
  </section>
</div>
</body>
</html>
```